Business Card Design Graduates

Slogan
"Practical Skills + Theory = Paid Job"

We assist Accounting Graduates to get work at the end of their University Degree by offering them a 6 week practical experience program.

At completion of the program they get business cards in their own Name, Title, phone numbers, address and email address. So, I need to be able to have a template where I can change these details and purchase business cards via Cardoloom or other outside printers.

I want it to be a bit colourful... ie not a plain white background or black, some blue would be nice. But it also needs to look professional as they will be meeting with future employers and networking. We help them get a paid job in Accounting at completion of the 6 week program.

Target Market(s)

Students and Employers

Industry/Entity Type

Business

Contact Information for Business Card

Marietta Dombrowski, Director, PO Box 418, Kelworth NSW 2174, Phone: 9482-3107 Fax: 9482-5921 Email: mariettad@harrowquill.com.au Web: www.HarrowquillWorkStart.com.au

Requirements
Must have
• changeable fields for me to change details for each student who graduates. The name of the company is already in the logo so no need to duplicate the name. Look at the website www.HarrowquillWorkStart.com.au because we expect the design should match our Corporate Image.

```html
<!DOCTYPE html>
<html lang="en">
<head>
<meta charset="utf-8">
<title>Graduate Business Card – Front and Back</title>
<link rel="stylesheet" href="https://fonts.googleapis.com/css2?family=Quicksand:wght@400;500;700&display=swap">
<style>
  :root {
    --backdrop: #e4e5e7;
    --card-blue: #2550a8;
    --card-blue-deep: #1f4597;
    --ink-silver: #c9ccd2;
    --icon-silver: #bfc3ca;
    --shadow: rgba(20, 30, 60, 0.22);
  }
  * { margin: 0; padding: 0; box-sizing: border-box; }
  html, body {
    width: 1200px;
    height: 1200px;
    overflow: hidden;
    background: var(--backdrop);
    font-family: "Quicksand", "Helvetica Neue", Arial, sans-serif;
  }
  .sheet {
    width: 1200px;
    height: 1200px;
    display: flex;
    flex-direction: column;
    align-items: center;
    justify-content: center;
    gap: 64px;
  }
  .card {
    position: relative;
    width: 700px;
    height: 424px;
    border-radius: 4px;
    background: linear-gradient(160deg, var(--card-blue) 0%, var(--card-blue-deep) 100%);
    box-shadow: 0 10px 28px var(--shadow);
    color: var(--ink-silver);
  }

  /* Front */
  .card-front {
    display: flex;
    flex-direction: column;
    align-items: center;
    justify-content: center;
  }
  .brand-mark {
    font-size: 76px;
    font-weight: 700;
    letter-spacing: 3px;
    line-height: 1;
    margin-top: -30px;
  }
  .slogan {
    margin-top: 58px;
    font-size: 27px;
    font-weight: 700;
    letter-spacing: 0.5px;
  }

  /* Back */
  .card-back {
    padding: 58px 0 0 0;
  }
  .holder {
    text-align: center;
    margin-bottom: 30px;
  }
  .holder-name {
    font-size: 32px;
    font-weight: 700;
    letter-spacing: 0.3px;
    line-height: 1.1;
  }
  .holder-title {
    font-size: 28px;
    font-weight: 400;
    letter-spacing: 1px;
    line-height: 1.1;
  }
  .contact-list {
    list-style: none;
    margin-left: 118px;
  }
  .contact-item {
    display: flex;
    align-items: center;
    gap: 14px;
    font-size: 21px;
    font-weight: 700;
    height: 40px;
    letter-spacing: 0.3px;
  }
  .contact-icon {
    width: 28px;
    height: 28px;
    flex: none;
  }
  .contact-icon circle { fill: var(--icon-silver); }
  .contact-icon .glyph { fill: var(--card-blue-deep); }
  .contact-icon .glyph-line { fill: none; stroke: var(--card-blue-deep); stroke-width: 1.8; stroke-linecap: round; stroke-linejoin: round; }
  .contact-item.is-web { letter-spacing: 0.8px; }
</style>
</head>
<body>
<main class="sheet">

  <section class="card card-front" aria-label="Business card front">
    <div class="brand-mark">LOGO</div>
    <p class="slogan">Practical Skills + Theory = Paid Job</p>
  </section>

  <section class="card card-back" aria-label="Business card back">
    <header class="holder">
      <h1 class="holder-name">Marietta Dombrowski</h1>
      <p class="holder-title">Director</p>
    </header>
    <ul class="contact-list">
      <li class="contact-item is-address">
        <svg class="contact-icon" viewBox="0 0 28 28" aria-hidden="true">
          <circle cx="14" cy="14" r="14"/>
          <path class="glyph" d="M14 5.5a6 6 0 0 0-6 6c0 4.5 6 11 6 11s6-6.5 6-11a6 6 0 0 0-6-6zm0 8.6a2.6 2.6 0 1 1 0-5.2 2.6 2.6 0 0 1 0 5.2z"/>
        </svg>
        <span>PO Box 418, Kelworth NSW 2174</span>
      </li>
      <li class="contact-item is-phone">
        <svg class="contact-icon" viewBox="0 0 28 28" aria-hidden="true">
          <circle cx="14" cy="14" r="14"/>
          <path class="glyph" d="M9.2 6.5l2.6-.4 1.6 4-1.8 1.4a10 10 0 0 0 4.9 4.9l1.4-1.8 4 1.6-.4 2.6c-.2 1-1.1 1.7-2.1 1.6C12.5 19.9 8.1 15.5 7.6 8.6c-.1-1 .6-1.9 1.6-2.1z"/>
        </svg>
        <span>9482-3107</span>
      </li>
      <li class="contact-item is-fax">
        <svg class="contact-icon" viewBox="0 0 28 28" aria-hidden="true">
          <circle cx="14" cy="14" r="14"/>
          <rect class="glyph" x="9.5" y="6" width="9" height="5" rx="0.6"/>
          <rect class="glyph" x="6.5" y="11.5" width="15" height="7" rx="1.2"/>
          <rect class="glyph" x="9.5" y="17" width="9" height="5" rx="0.6"/>
        </svg>
        <span>9482-5921</span>
      </li>
      <li class="contact-item is-email">
        <svg class="contact-icon" viewBox="0 0 28 28" aria-hidden="true">
          <circle cx="14" cy="14" r="14"/>
          <rect class="glyph" x="6.5" y="8.5" width="15" height="11" rx="1"/>
          <path class="glyph-line" d="M7 9.2l7 5.6 7-5.6" style="stroke:var(--icon-silver)"/>
        </svg>
        <span>mariettad@harrowquill.com.au</span>
      </li>
      <li class="contact-item is-web">
        <svg class="contact-icon" viewBox="0 0 28 28" aria-hidden="true">
          <circle cx="14" cy="14" r="14"/>
          <circle cx="14" cy="14" r="3.2" style="fill:none;stroke:var(--card-blue-deep);stroke-width:1.8"/>
          <path class="glyph-line" d="M17.2 11v4.3c0 1.4 2.8 1.6 3.3-.6a7.2 7.2 0 1 0-2.9 5.2"/>
        </svg>
        <span>www.HarrowquillWorkStart.com.au</span>
      </li>
    </ul>
  </section>

</main>
</body>
</html>
```